Restaurant Bar website in Oakland

Landing page that looks good on mobile and home. Easy to make changes to SEO and Menu page .
Might link with online ordering through the point of sale provider or not. Either way we want to be able to upload menus.
No forms need. Just landing page, about page with a paragraph and a few photos, address, hours and a mailto info@
A press page and an faq

Target Market(s)

Customers

Coding

Coded - Design and coding required

Number of Pages Required

4 page

Colors
00a990
ffc214

Requirements
Must have
• Simple to scroll
SEO
Simple to add menus
Our logo

```html
<!DOCTYPE html>
<html lang="en">
<head>
<meta charset="utf-8">
<title>Orwenna's Restaurant Bar</title>
<link rel="stylesheet" href="https://fonts.googleapis.com/css2?family=Josefin+Sans:wght@600;700&family=PT+Sans:wght@400;700&family=Roboto:wght@400&display=swap">
<style>
:root{
  --green:#2c5234;
  --gold:#c9a04c;
  --teal:#00a990;
  --yellow:#ffc214;
  --ink:#111110;
  --white:#ffffff;
  --text-dark:#2a2112;
  --head:"Josefin Sans",sans-serif;
  --body:"PT Sans",sans-serif;
  --copy:"Roboto",sans-serif;
}
*{margin:0;padding:0;box-sizing:border-box}
html,body{width:1200px;height:2892px;overflow:hidden}
body{position:relative;background:var(--ink);font-family:var(--body);color:var(--white)}
.abs{position:absolute}
a{color:inherit;text-decoration:none}

/* header */
.site-header{position:absolute;left:0;top:0;width:1200px;height:182px;background:var(--green)}
.contact-block{position:absolute;top:30px;color:var(--gold);font-weight:700;font-size:17px;line-height:25px;white-space:nowrap}
.contact-block.call{right:804px;text-align:right}
.contact-block.mail{left:792px}
.icon-ring{position:absolute;top:30px;width:52px;height:52px;border-radius:50%;border:3px solid var(--gold);display:flex;align-items:center;justify-content:center}
.icon-ring .dot{width:32px;height:32px;border-radius:50%;background:var(--gold);display:flex;align-items:center;justify-content:center}
.brand{position:absolute;left:490px;top:32px;width:220px;text-align:center;font-family:var(--head);font-weight:700;font-size:29px;letter-spacing:2px;color:var(--gold);line-height:50px;white-space:nowrap}
.nav-rule{position:absolute;top:147px;height:3px;background:var(--gold)}
.main-nav{position:absolute;left:403px;top:138px;display:flex;gap:47px;font-weight:700;font-size:17px;color:var(--gold)}
.main-nav .active{position:relative;color:#e6c98c}
.main-nav .active::after{content:"";position:absolute;left:50%;top:28px;margin-left:-9px;border:9px solid transparent;border-bottom-color:#e6c98c;border-top:0}
.slash{position:absolute;top:126px}

/* hero */
.hero{position:absolute;left:0;top:182px;width:1200px;height:554px;background:radial-gradient(ellipse at 50% 60%,#6a4a32 0%,#3b2a20 45%,#1d1a19 100%)}
.hero h1{position:absolute;left:0;top:196px;width:1200px;text-align:center;font-family:var(--head);font-weight:700;font-size:62px;line-height:60px;letter-spacing:1px;color:var(--white)}
.btn{position:absolute;width:152px;height:48px;border-radius:24px;border:3px solid;display:flex;align-items:center;justify-content:center;font-family:var(--head);font-weight:600;font-size:15px;letter-spacing:.5px}
.btn.hero-btn{left:524px;top:334px;border-color:var(--gold);background:var(--gold);box-shadow:inset 0 0 0 3px #3b2a20;color:var(--green)}
.btn.green-btn{left:524px;top:1087px;border-color:var(--green);background:var(--green);box-shadow:inset 0 0 0 3px var(--gold);color:var(--gold)}
.contact-tab{position:absolute;left:1147px;top:378px;width:53px;height:162px;background:var(--teal);display:flex;align-items:center;justify-content:center}
.contact-tab span{writing-mode:vertical-rl;font-weight:700;font-size:13px;letter-spacing:1px;color:var(--white)}

/* about */
.about{position:absolute;left:0;top:736px;width:1200px;height:490px;background:linear-gradient(180deg,#c79c4c,#d0a553)}
.section-rule{position:absolute;height:2px}
.section-title{position:absolute;left:0;width:1200px;text-align:center;font-family:var(--head);font-weight:700;font-size:36px;letter-spacing:1px}
.about p{position:absolute;left:215px;width:770px;text-align:center;font-family:var(--copy);font-size:13px;line-height:22.5px;color:#3a2c14}

/* gallery */
.dark-zone{position:absolute;left:0;top:1226px;width:1200px;height:1352px;background:radial-gradient(ellipse at 50% 40%,#222221,#0f0f0f)}
.card{position:absolute;width:316px;height:314px;background:var(--gold);padding:10px}
.card.featured{background:var(--teal)}
.card .photo{width:296px;height:226px}
.card h3{margin-top:18px;text-align:center;font-family:var(--head);font-weight:600;font-size:18px;letter-spacing:.5px;color:var(--text-dark)}
.card.featured h3{color:var(--white)}
.card p{margin-top:8px;text-align:center;font-family:var(--head);font-weight:700;font-size:12px;color:var(--text-dark)}
.card.featured p{color:var(--white)}
.tag{position:absolute;width:48px;height:18px;display:flex;align-items:center;justify-content:center;font-family:var(--head);font-weight:700;font-size:8px;letter-spacing:1px;clip-path:polygon(12% 0,88% 0,100% 50%,88% 100%,12% 100%,0 50%)}
.tag.outer{background:var(--green);color:var(--gold)}
.tag.inner{background:var(--yellow);color:var(--text-dark)}
.divider{position:absolute;left:111px;top:1887px;width:977px;height:1px;background:#4a4a48}

/* faq */
.faq-item{position:absolute;width:280px}
.faq-item h4{font-family:var(--head);font-weight:600;font-size:21px;line-height:26px;color:var(--white)}
.faq-item p{margin-top:12px;font-family:var(--copy);font-size:13px;line-height:22.5px;color:#e8e8e8}
.faq-item.right{text-align:right}
.faq-photo{position:absolute;left:442px;top:2106px;width:316px;height:384px;background:var(--gold);padding:5px}
.faq-photo div{width:100%;height:100%;background:linear-gradient(180deg,#3a2a22,#8a4a2a 55%,#5a3520)}
.v-line{position:absolute;width:1px;background:#6a6a66}

/* footer */
.site-footer{position:absolute;left:0;top:2578px;width:1200px;height:314px;background:var(--green)}
.footer-brand{position:absolute;left:111px;top:90px;font-family:var(--head);font-weight:700;font-size:32px;letter-spacing:2px;color:var(--gold);white-space:nowrap}
.footer-nav{position:absolute;left:473px;top:77px;display:flex;gap:47px;font-weight:700;font-size:17px;color:var(--gold)}
.info-icon{position:absolute;top:119px;width:56px;height:56px;border-radius:50%;background:var(--gold);display:flex;align-items:center;justify-content:center}
.info{position:absolute;top:124px}
.info h5{font-weight:700;font-size:16px;color:var(--white)}
.info p{margin-top:8px;font-family:var(--copy);font-size:13px;line-height:22px;color:var(--white)}
.info .big{font-size:17px;line-height:20px}
.footer-rule{position:absolute;left:111px;top:224px;width:977px;height:1px;background:#c9b98a}
.copyright{position:absolute;left:0;top:254px;width:1200px;text-align:center;font-family:var(--copy);font-size:16px;color:var(--white)}
</style>
</head>
<body>

<header class="site-header">
  <div class="contact-block call">Call us Today :<br>+1 510 555 0142</div>
  <div class="icon-ring" style="left:421px"><div class="dot">
    <svg width="16" height="16" viewBox="0 0 24 24"><path fill="#2c5234" d="M6.6 10.8a15 15 0 0 0 6.6 6.6l2.2-2.2c.3-.3.7-.4 1-.2 1.1.4 2.3.6 3.6.6.6 0 1 .4 1 1V20c0 .6-.4 1-1 1C10.6 21 3 13.4 3 4c0-.6.4-1 1-1h3.5c.6 0 1 .4 1 1 0 1.3.2 2.5.6 3.6.1.3 0 .7-.2 1z"/></svg>
  </div></div>
  <div class="brand">ORWENNA'S</div>
  <div class="icon-ring" style="left:722px"><div class="dot">
    <svg width="16" height="12" viewBox="0 0 16 12"><rect width="16" height="12" rx="1" fill="#2c5234"/><path d="M1 1l7 5 7-5" stroke="#c9a04c" stroke-width="1.5" fill="none"/></svg>
  </div></div>
  <div class="contact-block mail">Mail us Today :<br>hello@orwennabar.com</div>

  <div class="nav-rule" style="left:0;width:334px"></div>
  <div class="nav-rule" style="left:866px;width:334px"></div>
  <svg class="slash" style="left:346px" width="36" height="44"><path d="M18 2L2 42M34 2L18 42" stroke="#c9a04c" stroke-width="3"/></svg>
  <svg class="slash" style="left:818px" width="36" height="44"><path d="M2 2L18 42M18 2L34 42" stroke="#c9a04c" stroke-width="3"/></svg>
  <nav class="main-nav">
    <a class="active">HOME</a><a>ABOUT</a><a>PHOTO GALLERY</a><a>FAQ</a>
  </nav>
</header>

<section class="hero" role="img" aria-label="Photo of a warm-lit restaurant bar interior with dining tables and bar stools">
  <h1>WE ARE<br>RESTAURANT BAR</h1>
  <a class="btn hero-btn">LEARN MORE</a>
  <svg class="abs" style="left:587px;top:502px" width="26" height="26" viewBox="0 0 26 26"><circle cx="13" cy="13" r="11" stroke="#fff" stroke-width="2" fill="none"/><path d="M13 7v11M8 13l5 5 5-5" stroke="#fff" stroke-width="2" fill="none"/></svg>
</section>
<div class="contact-tab"><span>✆ CONTACT US</span></div>

<section class="about">
  <div class="section-rule" style="left:490px;top:100px;width:220px;background:var(--text-dark)"></div>
  <div class="section-rule" style="left:545px;top:92px;width:110px;background:var(--text-dark)"></div>
  <h2 class="section-title" style="top:118px;color:#1a1408">ABOUT US</h2>
  <p style="top:170px">Lorem ipsum dolor sit amet, consectetur adipiscing elit, sed do eiusmod tempor incididunt ut labore et dolore magna aliqua. Ut enim ad minim veniam, quis nostrud exercitation ullamco laboris nisi ut aliquip ex ea commodo consequat. Duis aute irure dolor in reprehenderit in voluptate velit esse cillum dolore eu fugiat nulla pariatur. Excepteur sint occaecat cupidatat non proident, sunt in culpa qui officia deserunt mollit anim id est laborum.</p>
  <p style="top:282px">Lorem ipsum dolor sit amet, consectetur adipiscing elit, sed do eiusmod tempor incididunt ut labore et dolore magna aliqua. Ut enim ad minim veniam, quis nostrud exercitation ullamco laboris nisi ut aliquip ex ea commodo</p>
</section>
<a class="btn green-btn">LEARN MORE</a>

<div class="dark-zone"></div>

<div class="section-rule" style="left:490px;top:1341px;width:220px;background:var(--gold)"></div>
<div class="section-rule" style="left:545px;top:1333px;width:110px;background:var(--gold)"></div>
<h2 class="section-title" style="top:1360px;color:var(--gold)">PHOTO GALLERY</h2>

<article class="card" style="left:68px;top:1420px">
  <div class="photo" role="img" aria-label="Photo of a server bringing plates to guests at a bar" style="background:linear-gradient(160deg,#5a3a24,#a06a3a 60%,#3a2618)"></div>
  <h3>LOREM IPSUM DOLOR SIT</h3><p>Commodo consequat</p>
</article>
<article class="card featured" style="left:441px;top:1463px">
  <div class="photo" role="img" aria-label="Photo of guests dining by candlelight in the bar" style="background:linear-gradient(160deg,#2a1e18,#6a4426 55%,#1a1410)"></div>
  <h3>LOREM IPSUM DOLOR SIT</h3><p>Commodo consequat</p>
</article>
<article class="card" style="left:814px;top:1420px">
  <div class="photo" role="img" aria-label="Photo of a pub bar counter with stools and shelves of bottles" style="background:linear-gradient(160deg,#6a4a2a,#b07a40 50%,#3a2a1a)"></div>
  <h3>LOREM IPSUM DOLOR SIT</h3><p>Commodo consequat</p>
</article>

<div class="tag outer" style="left:31px;top:1534px">PREV</div>
<div class="tag outer" style="left:372px;top:1534px">NEXT</div>
<div class="tag inner" style="left:403px;top:1577px">PREV</div>
<div class="tag inner" style="left:746px;top:1577px">NEXT</div>
<div class="tag outer" style="left:776px;top:1534px">PREV</div>
<div class="tag outer" style="left:1120px;top:1534px">NEXT</div>

<div class="divider"></div>

<div class="section-rule" style="left:490px;top:1992px;width:220px;background:var(--gold)"></div>
<div class="section-rule" style="left:545px;top:1984px;width:110px;background:var(--gold)"></div>
<h2 class="section-title" style="top:2012px;color:var(--gold)">FREQUENTLY ASKED QUESTIONS</h2>

<div class="faq-item" style="left:111px;top:2110px">
  <h4>1. Lorem ipsum dolor sit amet, consectetur</h4>
  <p>Lorem ipsum dolor sit amet, consectetur adipis cing elit, sed do eiusmod tempor incididunt ut labore et dolore</p>
</div>
<div class="faq-item" style="left:111px;top:2364px">
  <h4>2. Lorem ipsum dolor sit amet, consectetur</h4>
  <p>Lorem ipsum dolor sit amet, consectetur adipis cing elit, sed do eiusmod tempor incididunt ut labore et dolore</p>
</div>
<div class="faq-item right" style="left:808px;top:2110px">
  <h4>3. Lorem ipsum dolor sit<br>amet, consectetur</h4>
  <p>Lorem ipsum dolor sit amet, consectetur adipis cing elit, sed do eiusmod tempor incididunt ut labore et dolore</p>
</div>
<div class="faq-item right" style="left:808px;top:2364px">
  <h4>4. Lorem ipsum dolor sit<br>amet, consectetur</h4>
  <p>Lorem ipsum dolor sit amet, consectetur adipis cing elit, sed do eiusmod tempor incididunt ut labore et dolore</p>
</div>
<div class="v-line" style="left:425px;top:2106px;height:260px"></div>
<div class="v-line" style="left:775px;top:2232px;height:258px"></div>
<div class="faq-photo"><div role="img" aria-label="Photo of a dining room with wooden tables, pendant lamps and orange curtains"></div></div>

<footer class="site-footer">
  <div class="footer-brand">ORWENNA'S</div>
  <nav class="footer-nav"><a>HOME</a><a>ABOUT</a><a>PHOTO GALLERY</a><a>FAQ</a></nav>

  <div class="info-icon" style="left:366px">
    <svg width="14" height="18" viewBox="0 0 14 18"><path d="M7 0a7 7 0 0 0-7 7c0 5 7 11 7 11s7-6 7-11a7 7 0 0 0-7-7z" fill="#2c5234"/><circle cx="7" cy="7" r="2.5" fill="#c9a04c"/></svg>
  </div>
  <div class="info" style="left:441px"><h5>ADDRESS :</h5><p>Lorem ipsum dolor sit amet,<br>consectetur adipiscing</p></div>

  <div class="info-icon" style="left:632px">
    <svg width="18" height="18" viewBox="0 0 18 18"><circle cx="9" cy="9" r="7" stroke="#2c5234" stroke-width="2" fill="none"/><path d="M9 5v4l3 2" stroke="#2c5234" stroke-width="2" fill="none"/></svg>
  </div>
  <div class="info" style="left:707px"><h5>OPENING HOUR :</h5><p>Mon - Sat<br><span class="big">8am- 9pm</span></p></div>

  <div class="info-icon" style="left:864px">
    <svg width="18" height="13" viewBox="0 0 16 12"><rect width="16" height="12" rx="1" fill="#2c5234"/><path d="M1 1l7 5 7-5" stroke="#c9a04c" stroke-width="1.5" fill="none"/></svg>
  </div>
  <div class="info" style="left:939px"><h5>MAIL US :</h5><p>hello@orwennabar.com</p></div>

  <div class="footer-rule"></div>
  <p class="copyright">© 2021 Orwenna's Bar &nbsp;| All Rights Reserved | Terms and Conditions</p>
</footer>

</body>
</html>
```